Ferntop Contracting - Civil Construction Construction Company (Telecommunications)

Need a basic website to refine our branding to a current reflection of our service offerings. Ferntop Contracting provides civil construction services specializing in telecommunication sector.
I have started to create a website using word press. I would like to have someone refine the design and polish the overall look and functionality of the site. I would like to website to function in the wordpress format to allow for future edits and control of site.
Included site preview:
https://prv-hosts.pagebuildermock.example/7e2d90aa.com/Admin/index.html/qx_draft_preview
Coding
Coded - Design and coding required
Number of Pages Required
1 page
Look and feel
Each slider illustrates characteristics of the customer's brand and the style your logo design should communicate.

```html
<!DOCTYPE html>
<html lang="en">
<head>
<meta charset="utf-8">
<title>Ferntop Contracting</title>
<link rel="stylesheet" href="https://fonts.googleapis.com/css2?family=Poppins:wght@300;400;500;600&family=Russo+One&display=swap">
<style>
:root{--red:#e8141b;--dark:#1e1e1e;--ink:#222;--grey:#666;--line:#e3e3e3;--white:#fff}
*{box-sizing:border-box;margin:0;padding:0}
html,body{width:1200px;height:4326px;overflow:hidden}
body{position:relative;font-family:'Poppins',sans-serif;color:var(--ink);background:var(--white)}
.abs{position:absolute}
.btn{position:absolute;background:var(--red);color:#fff;border-radius:4px;font-size:13px;font-weight:500;display:flex;align-items:center;justify-content:center}
.brand{font-family:'Poppins',sans-serif;font-weight:400;font-size:30px;color:var(--ink);letter-spacing:.5px;white-space:nowrap}
.heading{position:absolute;width:100%;text-align:center;font-size:32px;font-weight:400;letter-spacing:.5px}
.heading b,.title b{font-family:'Russo One',sans-serif;font-weight:400}
.nav{top:117px;left:0;width:1200px;height:47px;background:var(--dark)}
.nav a{position:absolute;top:0;height:47px;color:#fff;font-size:13px;font-weight:500;display:flex;align-items:center;justify-content:center;text-decoration:none}
.nav .sep{position:absolute;top:12px;width:1px;height:23px;background:#444}
.hero{top:164px;left:0;width:1200px;height:616px;background:linear-gradient(180deg,#a9cbe6 0%,#d7e6f1 55%,#5f9a3d 78%,#3d7a25 100%)}
.hero-title{left:735px;top:230px;font-size:35px;line-height:42px;font-weight:500;color:#222;letter-spacing:.5px}
.hero-title span{color:var(--red)}
.dots{left:1157px;top:262px}
.dots i{display:block;width:8px;height:8px;border:1px solid #777;border-radius:50%;margin-bottom:7px}
.dots i.on{background:var(--red);border-color:var(--red)}
.why{top:1095px;width:300px;font-size:14px;line-height:16px;color:var(--grey);list-style:none}
.why li{position:relative;padding-left:18px}
.why li:before{content:"";position:absolute;left:0;top:5px;width:6px;height:6px;border-radius:50%;background:var(--red)}
.card{position:absolute;width:308px;height:278px;overflow:hidden}
.card .label{position:absolute;left:10px;right:10px;bottom:0;height:56px;background:var(--red);clip-path:polygon(3% 0,100% 0,100% 100%,0 100%);color:#fff;font-weight:600;font-size:15px;display:flex;align-items:center;justify-content:center;text-align:center;line-height:18px}
.work{top:2057px;left:0;width:1200px;height:783px;background:var(--dark)}
.arrow{position:absolute;width:34px;height:34px;border:2px solid #fff;border-radius:50%}
.field{position:absolute;border:1px solid var(--line);font-size:12px;color:#999;padding:12px 14px}
.footer{top:3930px;left:0;width:1200px;height:315px;background:var(--dark);color:#fff}
.flist{list-style:none;font-size:13px;line-height:22px}
.social{position:absolute;top:4264px;width:30px;height:30px;border-radius:50%}
</style>
</head>
<body>

<header>
  <div class="abs brand" style="left:113px;top:42px">Ferntop Contracting</div>
  <div class="btn" style="left:922px;top:40px;width:165px;height:44px">Get A Quote</div>
</header>

<nav class="abs nav">
  <a style="left:114px;width:119px;background:var(--red);border-radius:3px 3px 0 0">Home</a>
  <span class="sep" style="left:233px"></span>
  <a style="left:256px;width:200px">Why Choose Us</a>
  <span class="sep" style="left:465px"></span>
  <a style="left:465px;width:178px">Our Work</a>
  <span class="sep" style="left:643px"></span>
  <a style="left:643px;width:220px">Company Profile</a>
  <span class="sep" style="left:871px"></span>
  <a style="left:871px;width:158px">Contact</a>
  <span class="sep" style="left:1027px"></span>
  <svg class="abs" style="left:1074px;top:15px" width="18" height="18" viewBox="0 0 18 18"><circle cx="7" cy="7" r="5.5" fill="none" stroke="#fff" stroke-width="2"/><line x1="11" y1="11" x2="16" y2="16" stroke="#fff" stroke-width="2"/></svg>
</nav>

<section class="abs hero" role="img" aria-label="Red cable plow tractor carrying a reel of orange conduit on a grassy site under blue sky">
  <svg class="abs" style="left:0;top:0" width="1200" height="616" viewBox="0 0 1200 616">
    <polygon points="0,604 340,582 1140,616 0,616" fill="#fff"/>
    <polygon points="335,582 1200,500 1150,616 1140,616" fill="var(--red)"/>
  </svg>
  <div class="abs hero-title"><span>CIVIL</span> CONSTRUCTION<br>SERVICES</div>
  <div class="btn" style="left:737px;top:334px;width:165px;height:45px;justify-content:flex-start;padding-left:38px">Read More
    <svg class="abs" style="left:128px;top:11px" width="24" height="24" viewBox="0 0 24 24"><circle cx="12" cy="12" r="11" fill="#fff"/><path d="M7 12h9M12 8l4 4-4 4" fill="none" stroke="var(--red)" stroke-width="2"/></svg>
  </div>
  <div class="abs dots"><i></i><i class="on"></i><i></i><i></i></div>
</section>

<section>
  <h2 class="heading" style="top:850px"><b>WHY</b> CHOOSE US</h2>
  <svg class="abs" style="left:196px;top:978px" width="80" height="90" viewBox="0 0 80 90"><path d="M40 4 L76 16 V46 C76 68 58 82 40 88 C22 82 4 68 4 46 V16 Z" fill="var(--red)"/><path d="M60 20 L76 26 V46 C76 68 58 82 40 88 C36 86 32 84 28 82 Z" fill="#222"/></svg>
  <svg class="abs" style="left:550px;top:960px" width="95" height="95" viewBox="0 0 95 95"><rect x="2" y="58" width="60" height="18" rx="9" fill="var(--red)"/><rect x="6" y="36" width="40" height="20" fill="#222"/><rect x="14" y="24" width="22" height="14" fill="var(--red)"/><path d="M36 30 L66 6 L74 12 L50 40 Z" fill="var(--red)"/><path d="M66 6 L80 12 L86 40 L74 40 L70 20 Z" fill="#222"/></svg>
  <svg class="abs" style="left:920px;top:972px" width="100" height="86" viewBox="0 0 100 86"><path d="M4 24 L26 6 L50 20 L36 44 Z" fill="var(--red)"/><path d="M96 24 L74 6 L50 20 L64 44 Z" fill="#222"/><path d="M24 40 L50 20 L80 50 L62 72 Z" fill="var(--red)"/><circle cx="40" cy="64" r="5" fill="#222"/><circle cx="50" cy="72" r="5" fill="#222"/></svg>
  <ul class="abs why" style="left:114px"><li>Accredited health and safety program</li><li>Proven track record of safety excellence</li><li>Continuous training and development of employees</li></ul>
  <ul class="abs why" style="left:484px"><li>Productive and efficient crews</li><li>Current fleet of modern equipment</li><li>Use of latest construction techniques/ technologies</li></ul>
  <ul class="abs why" style="left:862px"><li>Quality and process driven</li><li>Excellent customer service</li><li>Privately owned and operated</li><li>Dependable, Reliable and Honest</li></ul>
</section>

<section>
  <h2 class="heading" style="top:1256px"><b>FTR</b> SERVICES</h2>
  <div class="card" style="left:115px;top:1334px;background:linear-gradient(160deg,#8b9aa6,#6b4a3a 55%,#b33a20)" role="img" aria-label="Directional drilling rig on a work site"><div class="label">DIRECTIONAL DRILLING</div></div>
  <div class="card" style="left:446px;top:1334px;background:linear-gradient(170deg,#9ab7d4,#7d7a6b 55%,#6a5a45)" role="img" aria-label="Trench digging crew with cable reels"><div class="label">TRENCH DIGGING AND<br>CABLE PLOWING</div></div>
  <div class="card" style="left:778px;top:1334px;background:linear-gradient(160deg,#c7cdd3,#8a8f96 60%,#b87040)" role="img" aria-label="Engineers reviewing plans on a site"><div class="label">ENGINEERING AND DESIGN</div></div>
  <div class="card" style="left:115px;top:1638px;background:linear-gradient(160deg,#a8c0cf,#4f5a4a 55%,#2e2e2e)" role="img" aria-label="Turn key equipment with truck in yard"><div class="label">TURN KEY SERVICES</div></div>
  <div class="card" style="left:446px;top:1638px;background:linear-gradient(170deg,#d7dde2,#9a9a9a 55%,#6f8a55)" role="img" aria-label="Hydrovac truck on roadside"><div class="label">HYDROVACING</div></div>
  <div class="card" style="left:778px;top:1638px;background:linear-gradient(160deg,#b4bfc8,#4aa3cf 50%,#5b6670)" role="img" aria-label="Fiber splicing machine close-up"><div class="label">FIBER/CABLE SPLICING</div></div>
</section>

<section class="abs work">
  <h2 class="heading" style="top:70px;color:#fff"><b>OUR</b> WORK</h2>
  <svg class="abs" style="left:548px;top:118px" width="92" height="10" viewBox="0 0 92 10"><polygon points="0,0 92,0 86,10 8,4" fill="var(--red)"/></svg>
  <div class="arrow" style="left:1046px;top:103px"><svg width="30" height="30" viewBox="0 0 30 30"><path d="M17 9l-6 6 6 6" fill="none" stroke="#fff" stroke-width="2"/></svg></div>
  <div class="arrow" style="left:1091px;top:103px"><svg width="30" height="30" viewBox="0 0 30 30"><path d="M13 9l6 6-6 6" fill="none" stroke="#fff" stroke-width="2"/></svg></div>
  <div class="abs" style="left:0;top:193px;width:290px;height:397px;background:linear-gradient(160deg,#3a3a2a,#4b3a1e);opacity:.7" role="img" aria-label="Yellow equipment with cable reel"></div>
  <div class="abs" style="left:891px;top:193px;width:309px;height:397px;background:linear-gradient(160deg,#4a4a4a,#6a6a6a);opacity:.7" role="img" aria-label="White service truck"></div>
  <div class="abs" style="left:290px;top:151px;width:601px;height:480px;background:linear-gradient(180deg,#b7cfe3 0%,#8a9a55 25%,#7d8a4a 60%,#6f7a3f 100%)" role="img" aria-label="Vibratory plow tractor laying conduit in a field with a worker">
    <div class="abs" style="left:0;width:601px;top:395px;text-align:center;color:#fff;font-size:15px;font-weight:500;line-height:20px">KELDOR VIBRATORY PLOW FOR LARGE PROJECTS /<br>CHALLENGING GROUND CONDITIONS</div>
  </div>
  <div class="btn" style="left:518px;top:671px;width:165px;height:45px">View More</div>
</section>

<section>
  <div class="abs" style="left:131px;top:2950px;width:432px;height:305px;background:linear-gradient(160deg,#5a6a5a,#8a8f95 50%,#d9dde0)" role="img" aria-label="Aerial view of company yard with fleet of white trucks"></div>
  <svg class="abs" style="left:131px;top:3253px" width="432" height="54" viewBox="0 0 432 54"><polygon points="0,2 432,2 400,52 0,22" fill="var(--red)"/></svg>
  <div class="abs" style="left:597px;top:2993px;width:50px;height:2px;background:var(--red)"></div>
  <h2 class="abs title" style="left:625px;top:2952px;font-size:28px;font-weight:400;line-height:34px"><b>ABOUT US</b></h2>
  <p class="abs" style="left:627px;top:3013px;width:465px;font-size:12.5px;line-height:26px;color:#444">Ferntop Contracting is a safety conscious, productive and efficient construction firm capable of all facets of civil construction. We have completed thousands of projects across Alberta, Saskatchewan and British Columbia working within various industry sectors. We have built a diverse team of skilled professionals who take a great deal of pride in their work and aim to achieve the highest levels of customer satisfaction.</p>
  <div class="btn" style="left:625px;top:3193px;width:165px;height:47px">Read More</div>
</section>

<section class="abs" style="left:185px;top:3397px;width:837px;height:325px;background:#fff;box-shadow:0 0 18px rgba(0,0,0,.12)">
  <h2 class="abs title" style="left:35px;top:32px;font-size:28px;font-weight:400"><b>QUICK CONTACT</b></h2>
  <div class="field" style="left:35px;top:85px;width:183px;height:44px">Name*</div>
  <div class="field" style="left:35px;top:135px;width:183px;height:44px">Phone*</div>
  <div class="field" style="left:35px;top:185px;width:183px;height:44px">Email*</div>
  <div class="field" style="left:222px;top:85px;width:183px;height:144px">Message</div>
  <div class="btn" style="left:35px;top:244px;width:183px;height:47px">Submit</div>
  <div class="abs" style="left:440px;top:28px;width:373px;height:273px;background:linear-gradient(160deg,#eef1ec,#e3eadf 60%,#dde6ef)" role="img" aria-label="Map showing the office location"></div>
</section>

<svg class="abs" style="left:0;top:3800px" width="1200" height="140" viewBox="0 0 1200 140">
  <polygon points="0,135 1200,60 1200,140 0,140" fill="var(--dark)"/>
  <polygon points="0,125 65,12 865,40 120,112" fill="var(--red)"/>
</svg>

<footer class="abs footer">
  <div class="abs brand" style="left:115px;top:65px;color:#fff">Ferntop Contracting</div>
  <svg class="abs" style="left:115px;top:142px" width="14" height="14" viewBox="0 0 14 14"><path d="M3 1l3 3-2 2c1 2 2 3 4 4l2-2 3 3-2 2C6 13 1 8 1 3z" fill="#fff"/></svg>
  <div class="abs" style="left:144px;top:138px;font-size:13px">1 (555) 014-2287</div>
  <svg class="abs" style="left:115px;top:166px" width="14" height="12" viewBox="0 0 14 12"><rect x="1" y="1" width="12" height="10" fill="none" stroke="#fff"/><path d="M1 1l6 5 6-5" fill="none" stroke="#fff"/></svg>
  <div class="abs" style="left:144px;top:161px;font-size:13px">info@ferntopcontracting.example</div>
  <svg class="abs" style="left:117px;top:200px" width="11" height="15" viewBox="0 0 11 15"><path d="M5.5 0C2.5 0 0 2.4 0 5.5 0 9.5 5.5 15 5.5 15S11 9.5 11 5.5C11 2.4 8.5 0 5.5 0z" fill="#fff"/><circle cx="5.5" cy="5.5" r="2" fill="var(--dark)"/></svg>
  <div class="abs" style="left:144px;top:197px;font-size:13px;line-height:22px">Harlow Ridge, AB T0E 1K4<br>Canada</div>

  <div class="abs" style="left:562px;top:70px;font-size:11px;font-weight:600">QUICK LINKS</div>
  <ul class="abs flist" style="left:562px;top:113px">
    <li>&gt;&nbsp; Home</li><li>&gt;&nbsp; About us</li><li>&gt;&nbsp; Our Services</li><li>&gt;&nbsp; Partners</li><li>&gt;&nbsp; Projects</li><li>&gt;&nbsp; Contact us</li>
  </ul>

  <div class="abs" style="left:830px;top:70px;font-size:11px;font-weight:600">NEWSLETTER</div>
  <div class="abs" style="left:830px;top:93px;width:38px;height:2px;background:#fff"></div>
  <div class="abs" style="left:830px;top:112px;width:270px;font-size:12px;line-height:14px">Subscribe to our newsletter to Recive latest news and update</div>
  <div class="abs" style="left:832px;top:156px;width:257px;height:36px;background:#fff;border-radius:3px;color:#666;font-size:12px;padding:9px 14px">Email address</div>
  <div class="btn" style="left:832px;top:204px;width:257px;height:36px;font-size:12px">Subscribe</div>
</footer>

<div class="abs" style="left:75px;top:4271px;font-size:12px;color:#333">Copyright © 2022 <span style="color:var(--red)">FERNTOP CONTRACTING</span>. All Rights Reserved.</div>
<span class="social" style="left:942px;background:var(--red)"></span>
<span class="social" style="left:980px;background:var(--dark)"></span>
<span class="social" style="left:1018px;background:var(--dark)"></span>
<span class="social" style="left:1058px;background:var(--dark)"></span>

</body>
</html>
```